Rollup banners

Need a design similar to the uploaded PDF file. Task is to create 3 designs to promote our school's qualifications.
1st Design should promote:
-KRB DIPLOMA IN FASHION TECHNOLOGY (APPAREL DESIGN AND PRODUCT DEVELOPMENT)
-KRB DIPLOMA IN FASHION TECHNOLOGY (MERCHANDISING AND MARKETING)
-KRB ADVANCED CERTIFICATE IN FASHION TECHNOLOGY (APPAREL DESIGN AND PRODUCT DEVELOPMENT)
-KRB ADVANCED CERTIFICATE IN FASHION TECHNOLOGY (MERCHANDISING AND MARKETING)
2nd Design:
-KRB DIPLOMA IN FASHION TECHNOLOGY (FOOTWEAR DESIGN AND PRODUCT DEVELOPMENT)
3rd Design:
Professional short Courses:
-Fashion Styling
-Sewing
-Fashion Entrepreneurship
-Leather Care
-Fabric Care
Background on our business(For your own knowledge): Our company is called Meridale Apparel Learning Hub (MaL.hb). We help train the fashion industry as well as over diploma programmes for people who are interested in joining the fashion industry.
Audience: General Public, Fashionistas, Fashion Students, Aspiring Footwear Enthusiasts and people interested to enter the fashion industry
Must Have:
-Take color scheme from uploaded PDF file
-Hex code for corporate color is #DA291C (Red)
- Corporate Colors to be Included: Grey, White, Black
Banner size: 850 X 2000mm
I've also attached our logos for you to use.
Please note that in the footer: please put the PJ NVR Centre, Brightmere Singapore.
You may choose to use either version of the logos- MaL.hb in Red ciricle or Typeface MaL.hb

```html
<!DOCTYPE html>
<html lang="en">
<head>
<meta charset="utf-8">
<title>Meridale Apparel Learning Hub – Rollup Banners</title>
<link rel="stylesheet" href="https://fonts.googleapis.com/css2?family=Open+Sans:wght@300;400;600;700&display=swap">
<style>
  :root {
    --brand-red: #E31E26;
    --panel-grey: #BEBFC1;
    --ink: #3A3A3A;
    --muted: #7A7A7A;
    --white: #FFFFFF;
    --frame: #D6D6D6;
    --font: "Open Sans", Arial, sans-serif;
  }
  * { box-sizing: border-box; margin: 0; padding: 0; }
  html, body { width: 1200px; height: 978px; overflow: hidden; background: var(--white); }
  body { position: relative; font-family: var(--font); }

  .banner {
    position: absolute; top: 51px; width: 334px; height: 837px;
    background: var(--white); border: 1px solid var(--frame); overflow: hidden;
  }
  .banner--programmes { left: 81px; }
  .banner--footwear { left: 455px; }
  .banner--short-courses { left: 816px; }

  .banner__art, .banner__photo { position: absolute; left: 0; top: 0; width: 334px; height: 771px; }

  .brand-name {
    position: absolute; right: 18px; top: 24px;
    display: flex; align-items: center; gap: 8px;
    color: var(--white); font-weight: 600; font-size: 13px; line-height: 16px; text-align: right;
  }
  .brand-name__mark { width: 14px; height: 14px; background: var(--brand-red); flex: none; }

  .headline {
    position: absolute; text-align: right; color: var(--brand-red);
    font-weight: 400; text-transform: uppercase;
  }
  .banner--programmes .headline { right: 28px; top: 291px; font-size: 31px; line-height: 39px; }
  .banner--footwear .headline { right: 14px; top: 410px; font-size: 29px; line-height: 38px; }
  .banner--short-courses .headline { right: 19px; top: 384px; font-size: 31px; line-height: 39px; }

  .course-list { position: absolute; list-style: none; text-align: right; color: var(--ink); font-weight: 600; white-space: nowrap; }
  .banner--programmes .course-list { right: 20px; top: 425px; font-size: 13.5px; line-height: 20px; text-transform: uppercase; letter-spacing: 0.2px; }
  .banner--programmes .course-list li + li { margin-top: 16px; }
  .banner--footwear .course-list { right: 17px; top: 596px; font-size: 18px; line-height: 30px; text-transform: uppercase; }
  .banner--short-courses .course-list { right: 23px; top: 584px; font-size: 17px; line-height: 29px; }

  .course-group-title {
    position: absolute; right: 23px; top: 545px; width: 208px; text-align: right;
    color: var(--muted); font-weight: 400; font-size: 16px; line-height: 22px;
    padding-bottom: 3px; border-bottom: 2px solid var(--muted);
  }

  .banner__footer {
    position: absolute; left: 0; bottom: 0; width: 100%; height: 66px;
    display: flex; align-items: center; justify-content: center; gap: 18px;
  }
  .accreditation__badge { width: 40px; height: 22px; border-radius: 3px; background: var(--panel-grey); }
  .accreditation--council .accreditation__badge { width: 26px; height: 26px; border-radius: 50%; background: var(--brand-red); }
  .accreditation { display: flex; align-items: center; gap: 4px; font-size: 8px; font-weight: 600; color: var(--ink); }
</style>
</head>
<body>

<section class="banner banner--programmes">
  <svg class="banner__art" viewBox="0 0 415 958" preserveAspectRatio="none" aria-hidden="true">
    <rect width="415" height="958" fill="var(--panel-grey)"/>
    <polygon points="0,802 0,958 90,958" fill="var(--brand-red)"/>
  </svg>
  <svg class="banner__photo" viewBox="0 0 415 958" preserveAspectRatio="none" role="img" aria-label="Photo of a tailor's dress form with a measuring tape">
    <defs>
      <linearGradient id="photo-dressform" x1="0" y1="0" x2="1" y2="1">
        <stop offset="0" stop-color="#C9C6C2"/>
        <stop offset="0.5" stop-color="#B8AD9E"/>
        <stop offset="1" stop-color="#A99B88"/>
      </linearGradient>
    </defs>
    <polygon points="0,0 415,0 0,807" fill="url(#photo-dressform)"/>
  </svg>
  <div class="brand-name"><span class="brand-name__mark"></span><span>Meridale Apparel<br>Learning Hub</span></div>
  <h2 class="headline">Step into<br>the world<br>of fashion</h2>
  <ul class="course-list">
    <li>-KRB Diploma in Fashion<br>Technology (Apparel Design<br>and Product Development)</li>
    <li>-KRB Diploma in Fashion<br>Technology (Merchandising<br>and Marketing)</li>
    <li>-KRB Advanced Certificate in<br>Fashion Technology (Apparel<br>Design and Product Development)</li>
    <li>-KRB Advanced Certificate in<br>Fashion Technology<br>(Merchandising and<br>Marketing)</li>
  </ul>
  <footer class="banner__footer">
    <div class="accreditation"><span class="accreditation__badge"></span>PJ NVR Centre</div>
    <div class="accreditation accreditation--council"><span class="accreditation__badge"></span>Brightmere Singapore</div>
  </footer>
</section>

<section class="banner banner--footwear">
  <svg class="banner__art" viewBox="0 0 415 958" preserveAspectRatio="none" aria-hidden="true">
    <rect width="415" height="958" fill="var(--panel-grey)"/>
    <polygon points="0,802 0,958 90,958" fill="var(--brand-red)"/>
  </svg>
  <svg class="banner__photo" viewBox="0 0 415 958" preserveAspectRatio="none" role="img" aria-label="Photo of a craftsman holding a tan leather brogue shoe">
    <defs>
      <linearGradient id="photo-shoe" x1="0" y1="0" x2="1" y2="1">
        <stop offset="0" stop-color="#3A2A22"/>
        <stop offset="0.45" stop-color="#B9743F"/>
        <stop offset="1" stop-color="#5A3B28"/>
      </linearGradient>
    </defs>
    <polygon points="0,0 415,0 415,317 0,657" fill="url(#photo-shoe)"/>
  </svg>
  <div class="brand-name"><span class="brand-name__mark"></span><span>Meridale Apparel<br>Learning Hub</span></div>
  <h2 class="headline">Footwear<br>design and<br>product<br>development</h2>
  <ul class="course-list">
    <li>KRB Diploma in Fashion<br>Technology (Footwear<br>Design and Product<br>Development)</li>
  </ul>
  <footer class="banner__footer">
    <div class="accreditation"><span class="accreditation__badge"></span>PJ NVR Centre</div>
    <div class="accreditation accreditation--council"><span class="accreditation__badge"></span>Brightmere Singapore</div>
  </footer>
</section>

<section class="banner banner--short-courses">
  <svg class="banner__art" viewBox="0 0 415 958" preserveAspectRatio="none" aria-hidden="true">
    <rect width="415" height="958" fill="var(--panel-grey)"/>
    <polygon points="0,802 0,958 90,958" fill="var(--brand-red)"/>
  </svg>
  <svg class="banner__photo" viewBox="0 0 415 958" preserveAspectRatio="none" role="img" aria-label="Fashion photo of a model in a black hat and striped black dress against a red and cream wall">
    <defs>
      <linearGradient id="photo-model" x1="0" y1="0" x2="1" y2="0">
        <stop offset="0" stop-color="#C8341E"/>
        <stop offset="0.45" stop-color="#2A2222"/>
        <stop offset="1" stop-color="#8E7F70"/>
      </linearGradient>
    </defs>
    <polygon points="0,0 415,0 415,297 0,657" fill="url(#photo-model)"/>
  </svg>
  <div class="brand-name"><span class="brand-name__mark"></span><span>Meridale Apparel<br>Learning Hub</span></div>
  <h2 class="headline">Step into<br>the world<br>of fashion</h2>
  <h3 class="course-group-title">Professional short Courses</h3>
  <ul class="course-list">
    <li>Fashion Styling</li>
    <li>Sewing</li>
    <li>Fashion Entrepreneurship</li>
    <li>Leather Care</li>
    <li>Fabric Care</li>
  </ul>
  <footer class="banner__footer">
    <div class="accreditation"><span class="accreditation__badge"></span>PJ NVR Centre</div>
    <div class="accreditation accreditation--council"><span class="accreditation__badge"></span>Brightmere Singapore</div>
  </footer>
</section>

</body>
</html>
```